Firm of surveyors needs a professional yet friendly looking flyer

Our company offers help to landlords who have a phone mast on their property. We help them to negotiate the best rent and lease terms. There are so many landlords who don't seek professional advice because they don't know it's available. We want to send them a flyer which is informative, looks professional but also friendly so it prompts them to call us. I have attached the wording and some pictures but have more I can send but they were too large to attach.

Target Market(s)

Ranges from farmers to large corporations and land owners

Industry/Entity Type

Surveyor

Font styles to use
Sans Serif

Colors
acd136
9bcb3c
000000
ffffff
606060
848484

Requirements
Must have
• Must be clear, must give a professional look, must include pictures, must include our logo, must use our colour scheme (or variations of it). Ideally, I would like a try-fold design if possible.
Nice to have
• I would like there to be stand out lines to catch the readers eye (I have included some on the wording document). I would like a clean and modern design
Should not have
• Should not be too fussy

```html
<!DOCTYPE html>
<html lang="en">
<head>
<meta charset="utf-8">
<title>Mast Rent Company – Tri-fold Flyer</title>
<link rel="stylesheet" href="https://fonts.googleapis.com/css2?family=Arimo:wght@400;700&family=Roboto+Condensed:wght@400&display=swap">
<style>
  :root {
    --green: #5f9732;
    --green-bright: #9bcb3c;
    --green-light: #acd136;
    --black: #000000;
    --white: #ffffff;
    --grey-dark: #606060;
    --grey-mid: #848484;
    --text: #1e1e1e;
    --paper: #f7f7f7;
    --stage: #e4e5e6;
  }
  * { box-sizing: border-box; margin: 0; padding: 0; }
  html, body { width: 1200px; height: 800px; overflow: hidden; }
  body {
    background: var(--stage);
    font-family: "Arimo", Arial, sans-serif;
    color: var(--text);
  }
  .brochure {
    position: absolute; left: 120px; top: 27px;
    width: 960px; height: 746px;
    display: flex;
    box-shadow: 0 10px 30px rgba(0,0,0,.15);
  }
  .panel {
    width: 320px; height: 746px;
    background: var(--paper);
    position: relative;
    border-right: 1px solid #e2e2e2;
  }
  .panel:last-child { border-right: none; }
  .body-text {
    position: absolute;
    font-size: 12px; line-height: 14.5px;
    text-align: justify; hyphens: auto;
  }
  .body-text p + p { margin-top: 14px; }
  .highlight { color: var(--green); }

  /* About panel */
  .about-tab {
    position: absolute; right: 0; top: 34px;
    width: 186px; height: 36px;
    background: var(--green);
    border-radius: 18px 0 0 18px;
    color: var(--white);
    font-weight: 700; font-size: 23px;
    line-height: 36px; padding-left: 28px;
  }
  .about .body-text { top: 86px; left: 25px; right: 28px; }

  /* Photo band */
  .photo-band {
    position: absolute; left: 0; top: 0; width: 100%;
    height: 125px;
    background: linear-gradient(180deg, #a9c7e3 0%, #d9e6ee 55%, #8fae5c 75%, #5e8a35 100%);
  }
  .icon-badge {
    position: absolute; left: 50%;
    width: 106px; height: 106px; margin-left: -53px;
    border-radius: 50%;
    background: var(--green);
    border: 5px solid var(--grey-dark);
  }
  .icon-badge.top { top: 78px; }
  .icon-badge.lower { top: 412px; }
  .pill {
    position: absolute; left: 50%;
    height: 36px; border-radius: 18px;
    color: var(--white); font-weight: 700;
    text-align: center; line-height: 36px;
  }
  .pill.dark { background: var(--black); font-size: 21px; width: 276px; margin-left: -138px; top: 194px; }
  .pill.grey { background: var(--grey-dark); font-size: 21px; width: 280px; margin-left: -140px; top: 525px; }
  .pill.grey.small { font-size: 16.5px; width: 278px; margin-left: -139px; top: 194px; }
  .service .text-upper { top: 242px; left: 28px; right: 29px; }
  .service .text-lower { top: 572px; left: 26px; right: 30px; }
  .climate .body-text { top: 242px; left: 27px; right: 24px; }

  .accent-rule {
    position: absolute; left: 0; top: 626px;
    width: 112px; height: 4px; background: var(--green);
  }
  .callout {
    position: absolute; left: 36px; right: 14px; top: 640px;
    font-family: "Roboto Condensed", "Arial Narrow", sans-serif;
    color: var(--green); font-size: 17px; line-height: 22px;
  }
</style>
</head>
<body>
<main class="brochure">

  <section class="panel about">
    <h2 class="about-tab">About Us</h2>
    <div class="body-text">
      <p><span class="highlight">The Mast Rent Company is a firm of telecoms surveyors with over 15 years' experience of dealing with mobile phone mast operators.</span> We have built up a massive database of thousands of comparable mobile phone mast deals to aid us in our telecoms negotiations. All our surveyors have spent time working for phone mast operators and know the industry inside out. We now work exclusively for landlords, fighting your corner, ensuring our landlords get the highest rents and best lease terms available in the market place.</p>
      <p>Many of the original mobile phone mast leases / agreements are now coming up for renewal. This is an ideal opportunity for landlords to achieve the best deal. <span class="highlight">We are currently offering to review telecoms leases for free and provide landlords with our recommendations.</span> If you would like to take us up on this free no obligation offer, send a copy of your agreement and any recent correspondence to us, either via post or email using the details on this flyer. Please also provide us with your name, contact number and let us know the current rent you are achieving so we can see if there is room for improvement. Once we have received this, one of our surveyors will give you a call when convenient to talk through your lease with you, highlighting anything we feel needs addressing, any opportunity to increase the rent, or to discuss a specific issue you are having with your mast (i.e. an upgrade request).</p>
      <p>Recently, operators have been attempting to cut costs by reducing rents. They are joining forces in an effort to drive rents down. Many landlords are contacting us after receiving a letter from the operators / operator's agent, telling them they must accept a rent reduction or risk losing their site. In the majority of cases, The Mast Rent Company can prevent this from occurring and protect the landlord's rental income.</p>
    </div>
  </section>

  <section class="panel service">
    <div class="photo-band" role="img" aria-label="Photo of a telecoms mast compound in green farmland"></div>
    <div class="icon-badge top" role="img" aria-label="Icon for selling a phone mast"></div>
    <h2 class="pill dark">Sell Your Phone Mast</h2>
    <div class="body-text text-upper">
      <p>We can also assist landlords in selling their phone mast. We have strong links with many large investors who regularly purchase the freehold or leasehold interest of masts and will pay a cash lump sum of tens, even hundreds of thousands of pounds. This can be done in a matter of weeks and the cash is yours to spend however you like, regardless of whether the mast stays for the duration of the investors leasehold or not. We can negotiate flexible terms, such as a buyback option so please call us today to discuss.</p>
    </div>
    <div class="icon-badge lower" role="img" aria-label="Icon for getting a phone mast"></div>
    <h2 class="pill grey">Getting A Phone Mast</h2>
    <div class="body-text text-lower">
      <p>If you don't currently have a mast located on your land but are interested in receiving thousands of pounds a year in rental income, or you have a redundant mast you would like to market, we offer a free advertising service on our website. We will market your land to phone mast operators with a view to having a mast located there. Please visit the 'Advertise My Site' link on our website to take advantage of this service.</p>
    </div>
  </section>

  <section class="panel climate">
    <div class="photo-band" role="img" aria-label="Photo of a lattice phone mast against a blue sky over fields"></div>
    <div class="icon-badge top" role="img" aria-label="Icon for the telecoms climate"></div>
    <h2 class="pill grey small">The current telecoms climate</h2>
    <div class="body-text">
      <p>The telecoms market, in relation to mobile phone masts, is going through some huge changes. Operators are combining to cut costs. We have already seen Trinet join forces with Telmo and Oxan form a jointly owned company with Vocalis called STL. More recently, Telmo and Citrine have merged to form Allcover Networks Ltd to become the new network leader. What this can mean for the landlord is changes to their site and potentially the loss of income. It can all be very confusing but don't worry, this is where we can help. We know the telecoms industry and understand how a new situation may affect a landlord, therefore, allowing us to provide the best advice on protecting your asset.</p>
      <p>In April 2017, the Government introduced the Digital Economy Act. This sets out significant changes for landlords, including the way rents are calculated. We have already seen operators contact landlords, trying to reduce their rent in light of this new law. We are working alongside specialist telecoms solicitors to try to reduce the potential negative impact on landlords.</p>
    </div>
    <div class="accent-rule"></div>
    <p class="callout">Interested in selling your site? Or already have an offer? We can help you to achieve the best sale price, quickly</p>
  </section>

</main>
</body>
</html>
```